Korvane 24/7 Gym & Health Bar Webpage

We need a professional and interactive webpage for a 24/7 health club.
Our approach is professional yet friendly offering holitic professional services for both general and special populations, along with flexible 24/7 gym and group fitness memberships. Professional services that we offer;
Exercise Physiologist
Strength & Conditioning
Physiotherapy
Chiropractor
Nutrition
Personal Training
we also service acute and chronic injuries, work cover, and veteran affairs

We also have a well-being bar offers healthy food, beverages and wide range of supplements.
We send out regular newsletters and want it to be interactive with social media and e-commerce.
Final design should demonstrate a holistic approach where clients have access to a wide range of health services within a professional health club environment. needs to be phone and table friendly please

i have attached a template i had been working on but wasn't happy with it

Target Market(s)

wide demographic including:

Special population - older demographic looking for professional services. Doctors will be referring clients to us also

24/7 gym - aged 25+ yrs, male and female

Industry/Entity Type

Health And Wellness

Coding

Coded - Design and coding required

Number of Pages Required

5+ page

Colors
33a6d7
add136
ffffff
0355a3

Requirements
Must have
• atmosphere and professionalism whilst inviting and sincere
• social media interaction & blog page
• clear navigation
• mobile and table friendly
• Brisk E-newsletter sign up
• testimonials
Nice to have
• customer feedback option
• FAQ
• opportunity to integrate online shop
• ability to download free visit pass

```html
<!DOCTYPE html>
<html lang="en">
<head>
<meta charset="utf-8">
<title>Korvane 24/7 Gym &amp; Health Bar</title>
<link rel="stylesheet" href="https://fonts.googleapis.com/css2?family=Open+Sans:wght@400;600;700&family=Oswald:wght@400;500&family=Raleway:wght@400;500;600&display=swap">
<style>
:root{
  --green:#a8cf33;
  --green-dark:#8fb323;
  --blue:#33a6d7;
  --navy:#0355a3;
  --white:#ffffff;
  --ink:#333333;
  --muted:#555555;
  --footer:#262626;
  --footer-line:#3a3a3a;
}
*{margin:0;padding:0;box-sizing:border-box}
html,body{width:1200px;height:2983px;overflow:hidden}
body{font-family:"Open Sans",Arial,sans-serif;color:var(--ink);background:var(--white);position:relative}

/* Hero */
.hero{position:absolute;left:0;top:0;width:1200px;height:547px;
  background:radial-gradient(ellipse at 62% 35%,#8a7a62 0%,#4e4335 35%,#241e18 75%,#141210 100%)}
.topbar{position:absolute;left:0;top:0;width:1200px;height:27px;background:rgba(20,20,20,.85);
  color:#ddd;font-size:11px;display:flex;align-items:center;padding:0 189px}
.topbar .contact{display:flex;align-items:center;gap:6px}
.topbar .account{margin-left:auto;display:flex;gap:18px}
.header{position:absolute;left:166px;top:36px;width:862px;height:67px;background:var(--white);
  display:flex;align-items:center;padding:0 16px}
.brand{display:flex;align-items:center;gap:10px}
.brand .mark{width:30px;height:30px;border-radius:50%;background:var(--blue)}
.brand .name{font-weight:700;font-size:26px;color:var(--navy);letter-spacing:.5px;line-height:28px}
.brand .tag{display:block;font-size:9px;color:var(--navy);font-weight:700;letter-spacing:0;line-height:12px}
.nav{margin-left:auto;display:flex}
.nav a{font-size:12px;font-weight:700;color:#333;text-decoration:none;padding:0 12px;line-height:67px}
.nav a.active{color:var(--green)}
.hero-title{position:absolute;left:189px;top:205px;font-family:"Oswald",sans-serif;font-weight:400;
  font-size:34px;line-height:46px;color:var(--white);width:420px}
.hero-text{position:absolute;left:189px;top:312px;width:400px;font-size:14px;line-height:20px;color:#f0f0f0;font-weight:600}
.btn{position:absolute;left:189px;top:386px;background:var(--green);color:var(--white);font-size:12px;font-weight:700;
  padding:11px 22px;border-radius:2px}

/* Welcome */
.section-title{position:absolute;left:0;width:1200px;text-align:center;font-family:"Raleway",sans-serif;font-weight:500;color:var(--green)}
.welcome-title{top:585px;font-size:38px;letter-spacing:1px}
.welcome-sub{position:absolute;top:645px;left:360px;width:480px;text-align:center;font-size:16px;font-weight:600;color:#333;line-height:24px;text-transform:uppercase}
.card{position:absolute;width:259px}
.card .photo{width:259px;height:158px}
.card h3{font-family:"Raleway",sans-serif;font-weight:500;font-size:17px;color:var(--green);text-align:center;margin-top:18px;text-transform:uppercase}
.card p{font-size:12px;line-height:17px;color:#444;text-align:center;margin-top:8px;padding:0 12px}

/* Quote band */
.quote-band{position:absolute;left:0;top:1319px;width:1200px;height:538px;
  background:linear-gradient(100deg,#4a5560 0%,#8d96a0 25%,#c9c3bb 50%,#d9cbb9 70%,#7b7167 100%)}
.quote{position:absolute;left:0;top:1535px;width:1200px;text-align:center;font-weight:700;
  font-size:40px;line-height:52px;color:var(--green);text-transform:uppercase}

/* About */
.about-title{top:1893px;font-size:30px}
.about-text{position:absolute;left:270px;top:1962px;width:660px;text-align:center;font-size:16px;line-height:26px;color:#333}

/* Testimonials */
.testi-band{position:absolute;left:0;top:2088px;width:1200px;height:438px;
  background:linear-gradient(90deg,#5a3a3c 0%,#8c6a6a 30%,#6d5b58 60%,#3f3536 100%)}
.bubble{position:absolute;top:2188px;width:262px;height:132px;background:var(--green);color:var(--white);
  font-size:11px;line-height:17px;text-align:center;padding:18px 16px}
.bubble::after{content:"";position:absolute;left:34px;bottom:-16px;border-left:16px solid var(--green);border-bottom:16px solid transparent}
.person{position:absolute;top:2350px;display:flex;align-items:center;gap:10px}
.person .avatar{width:60px;height:60px;border-radius:50%;border:3px solid var(--white);background:linear-gradient(135deg,#c9a68c,#7a5a48)}
.person .who b{display:block;font-size:14px;color:var(--white);font-weight:600}
.person .who span{font-size:11px;color:#e6e6e6}
.dots{position:absolute;left:580px;top:2476px;display:flex;gap:6px}
.dots i{width:8px;height:8px;border-radius:50%;background:#ccc}
.dots i.on{background:var(--green)}

/* Gallery */
.gallery-title{top:2552px;font-size:30px}
.gallery-photo{position:absolute;top:2636px;width:192px;height:132px}

/* Footer */
.footer{position:absolute;left:0;top:2818px;width:1200px;height:165px;background:var(--footer)}
.f-col{position:absolute;top:2845px;color:var(--white);text-align:center}
.f-col h4{font-family:"Raleway",sans-serif;font-weight:500;font-size:17px}
.socials{display:flex;gap:34px;justify-content:center;margin-top:22px}
.socials i{width:12px;height:12px;border-radius:50%;background:var(--white);display:block}
.signup{display:flex;margin-top:16px;justify-content:center}
.signup .field{width:150px;height:26px;background:var(--green);font-size:9px;color:#333;line-height:26px;text-align:left;padding-left:8px}
.signup .go{width:26px;height:26px;background:var(--white);display:flex;align-items:center;justify-content:center}
.address{font-size:13px;margin-top:22px;color:#ddd}
.copyright{position:absolute;left:0;top:2952px;width:1200px;text-align:center;font-size:10px;color:#aaa;border-top:1px solid var(--footer-line);padding-top:10px}
</style>
</head>
<body>

<section class="hero" role="img" aria-label="Athlete training with a skipping rope in a sunlit warehouse gym"></section>
<div class="topbar">
  <span class="contact">
    <svg width="11" height="11" viewBox="0 0 24 24"><path fill="#ddd" d="M6.6 10.8a15 15 0 0 0 6.6 6.6l2.2-2.2c.3-.3.7-.4 1-.2 1.1.4 2.3.6 3.6.6.6 0 1 .4 1 1V20c0 .6-.4 1-1 1A17 17 0 0 1 3 4c0-.6.4-1 1-1h3.5c.6 0 1 .4 1 1 0 1.3.2 2.5.6 3.6.1.3 0 .7-.2 1z"/></svg>
    Any Questions? Call us: 1-555-010-2244
  </span>
  <span class="account"><span>Member Login</span><span>Register</span></span>
</div>
<header class="header">
  <div class="brand">
    <span class="mark"></span>
    <span class="name">Korvane<span class="tag">24/7 Gym &amp; Health Bar</span></span>
  </div>
  <nav class="nav">
    <a class="active">HOME</a><a>ABOUT</a><a>OUR PACKAGES</a><a>SERVICES</a><a>BLOG</a><a>FAQ</a><a>CONTACT US</a>
  </nav>
</header>
<h1 class="hero-title">Human Body Is The Best Picture Of Human Soul</h1>
<p class="hero-text">Train any hour with coaches who care about your progress. Your health journey starts here.</p>
<span class="btn">JOIN NOW</span>

<h2 class="section-title welcome-title">WELCOME TO FITNESS</h2>
<p class="welcome-sub">We are a New York based fitness house. We work towards making people fit and healthy</p>

<article class="card" style="left:189px;top:746px">
  <div class="photo" role="img" aria-label="Group cardio class on exercise bikes" style="background:linear-gradient(135deg,#d96a5a,#f2d4c8 50%,#8a8a90)"></div>
  <h3>Cardio Training</h3>
  <p>Guided intervals on bikes, rowers and treadmills to lift your heart rate and build lasting stamina.</p>
</article>
<article class="card" style="left:470px;top:746px">
  <div class="photo" role="img" aria-label="Barbell resting on a bench in a weights room" style="background:linear-gradient(135deg,#1e1e1e,#6e6e6e 50%,#2a2a2a)"></div>
  <h3>Strength Training</h3>
  <p>Coached lifting sessions that build muscle, protect joints and improve everyday strength safely.</p>
</article>
<article class="card" style="left:752px;top:746px">
  <div class="photo" role="img" aria-label="Yoga plank pose on a mat" style="background:linear-gradient(135deg,#f4ece4,#d9b8a0 55%,#b07a5e)"></div>
  <h3>Yoga Training</h3>
  <p>Gentle flows and deep stretches that restore balance, ease tension and support recovery.</p>
</article>
<article class="card" style="left:189px;top:1028px">
  <div class="photo" role="img" aria-label="Red punching bags and boxing gloves" style="background:linear-gradient(135deg,#e9e4de,#b83a30 55%,#5a1c18)"></div>
  <h3>Indoor Boxing</h3>
  <p>Bag work and pad drills that sharpen footwork, burn energy and release the stress of the day.</p>
</article>
<article class="card" style="left:470px;top:1028px">
  <div class="photo" role="img" aria-label="Fresh vegetables and fruit on a table" style="background:linear-gradient(135deg,#4f8a2a,#c8a234 45%,#b8402a 75%,#3d6a22)"></div>
  <h3>Nutrition</h3>
  <p>Practical meal plans from our team that fit your goals, your budget and your busy week.</p>
</article>
<article class="card" style="left:752px;top:1028px">
  <div class="photo" role="img" aria-label="Colourful supplement capsules" style="background:linear-gradient(135deg,#e8a42a,#d8462e 40%,#7fb83a 70%,#e6c84a)"></div>
  <h3>Supplements</h3>
  <p>A wide range of proteins, vitamins and recovery blends at our health bar, open around the clock.</p>
</article>

<section class="quote-band" role="img" aria-label="Members riding exercise bikes in a bright spin studio"></section>
<p class="quote">&ldquo;Human body is the best picture<br>of human soul&rdquo;</p>

<h2 class="section-title about-title">About Korvane Health And Fitness</h2>
<p class="about-text">Our club brings exercise physiology, physiotherapy, strength coaching and nutrition under one roof. Members train 24/7 while our professionals guide every step, from injury recovery to peak performance.</p>

<section class="testi-band" role="img" aria-label="Members working out together in the gym, softly blurred"></section>
<blockquote class="bubble" style="left:182px">&ldquo;The physio and coaches worked together on my knee. Six months on I am lifting again and feel stronger than ever before.&rdquo;</blockquote>
<blockquote class="bubble" style="left:468px">&ldquo;Open all night means I can train after my shift. Friendly staff, spotless floor and the smoothies at the bar are great.&rdquo;</blockquote>
<blockquote class="bubble" style="left:756px">&ldquo;My doctor referred me here for back pain. The exercise physiologist built a plan I can follow and I move freely again.&rdquo;</blockquote>
<div class="person" style="left:250px"><span class="avatar" role="img" aria-label="Portrait of Tom Hadley"></span><span class="who"><b>Tom Hadley</b><span>NY, USA</span></span></div>
<div class="person" style="left:536px"><span class="avatar" role="img" aria-label="Portrait of Lena Ortiz"></span><span class="who"><b>Lena Ortiz</b><span>Eastbrook, USA</span></span></div>
<div class="person" style="left:824px"><span class="avatar" role="img" aria-label="Portrait of Priya Nandel"></span><span class="who"><b>Priya Nandel</b><span>NY, USA</span></span></div>
<div class="dots"><i class="on"></i><i></i><i></i></div>

<h2 class="section-title gallery-title">Gallery</h2>
<div class="gallery-photo" role="img" aria-label="Spin class on bikes" style="left:182px;background:linear-gradient(135deg,#3a4a5a,#c9b8a8 60%,#6a5a50)"></div>
<div class="gallery-photo" role="img" aria-label="Stretching on a yoga mat" style="left:398px;background:linear-gradient(135deg,#f2ece6,#d8a88a 60%,#a06a50)"></div>
<div class="gallery-photo" role="img" aria-label="Group fitness class with hand weights" style="left:613px;background:linear-gradient(135deg,#5a2a3a,#c25a6a 50%,#2a2a2a)"></div>
<div class="gallery-photo" role="img" aria-label="Trainer coaching a member on weights" style="left:822px;background:linear-gradient(135deg,#2a2a2a,#8a7a70 55%,#4a4040)"></div>

<footer class="footer"></footer>
<div class="f-col" style="left:170px;width:230px">
  <h4>Let&rsquo;s Stay Connected</h4>
  <div class="socials"><i></i><i></i><i></i><i></i></div>
</div>
<div class="f-col" style="left:470px;width:230px">
  <h4>Join The Newsletter</h4>
  <div class="signup">
    <span class="field">Enter Your Email Address</span>
    <span class="go"><svg width="10" height="10" viewBox="0 0 10 10"><path d="M2 1l5 4-5 4" stroke="#333" stroke-width="1.6" fill="none"/></svg></span>
  </div>
</div>
<div class="f-col" style="left:770px;width:290px">
  <h4>Our Address</h4>
  <p class="address">48 Larkfield Road, Eastbrook NY, USA</p>
</div>
<p class="copyright">&copy; Copyright 2016 Korvane Health Fitness. All rights reserved</p>

</body>
</html>
```